QR248 - Plan, Guard, Track, Steer - OT Cyber Security Software, KPI Visualisation Software and

Build Website - we require a website with approx 5 tabs on scrolling pane screen - Home, Who We are, Cyber Security, Visualisation, Trusted Partners, Support, Contact, single scrolling panel or tab click to page with images and 2-3 paragraphs of text - wording and links to partners will be provided along with company logo

Target Market(s)

Process Control Markets - Oil and Gas clients, Telecommunications Operators, IOT companies, manufacturing, transport sector etc

Industry/Entity Type

Security

Coding

Coded - Design and coding required

Number of Pages Required

5+ page

Font styles to use
Sans Serif

Colors
0255a3
3176b5
85abd2
f04a50
ec1f27
1b1b1b
474747
919191
d3d3d3

Requirements
Must have
• Scrolling pane / page with tabs along the top -
• Who We are - software and professional services provider for Process Control Cyber Security and Data visualisation
• Plan Guard Track Steer -
• define and defend process control networks, measure, manage, visualise data sets from any source etc
• Process Control Cyber Security - images and wording - area for wording can be created and left to be fully populated etc
• Visualisation - data set visualisation from desk top / tablet / mobile device,
• Trusted Partners - links to www.belvanta.example www.korinex.example www.drumelo.example.au
• Support
• Contact Details
• images for cyber security risks etc
• data visualisation / visual KPI - software package
• Support - link to www.drumelo.example.au for NOC and Customer Support - sections for Gold, Silver and Bronze support package - we will add wording later
Nice to have
• Colours - blues / blacks / grey - cyber security information and sections,
• reds etc for visualisation sections
• Use similar colours as logo for rest of pages

```html
<!DOCTYPE html>
<html lang="en">
<head>
<meta charset="utf-8">
<title>QR248 – Plan, Guard, Track, Steer</title>
<link href="https://fonts.googleapis.com/css2?family=Oswald:wght@500&family=Poppins:wght@300;400;500;600&display=swap" rel="stylesheet">
<style>
:root{
  --blue-deep:#0255a3;
  --blue:#3176b5;
  --blue-soft:#85abd2;
  --red:#f04a50;
  --red-strong:#ec1f27;
  --ink:#1b1b1b;
  --text:#474747;
  --muted:#919191;
  --line:#d3d3d3;
  --pale-blue:#eaf3fd;
  --pale-grey:#efefef;
  --navy:#0c2a55;
  --white:#ffffff;
}
*{box-sizing:border-box;margin:0;padding:0}
html,body{width:1200px;height:3475px;overflow:hidden}
body{font-family:"Poppins",sans-serif;color:var(--text);background:var(--white);position:relative}
section,header,footer{position:relative;width:1200px;overflow:hidden}
.wrap{position:absolute;left:86px;width:1028px}
h2{font-family:"Poppins",sans-serif;font-weight:500;color:var(--ink);font-size:30px}
.rule{display:block;width:44px;height:2px;background:var(--red);margin-top:12px}
p{font-size:14px;line-height:24px}

/* hero */
.hero{height:598px}
.hero-bg{position:absolute;inset:0;background:radial-gradient(ellipse at 45% 40%,#5a86a8 0%,#2f5679 40%,#15304c 80%,#0e2238 100%)}
.nav{position:absolute;top:22px;left:86px;right:86px;display:flex;align-items:center;justify-content:space-between}
.brand{display:flex;align-items:center;gap:12px;color:var(--white);font-weight:600;font-size:22px}
.brand-mark{width:30px;height:30px;background:var(--red)}
.menu{display:flex;gap:0;list-style:none}
.menu li{font-size:15px;color:var(--white);padding:6px 15px}
.menu li.active{border:1px solid var(--red);border-radius:3px}
.hero-title{position:absolute;top:258px;width:100%;text-align:center;color:var(--white)}
.hero-title h1{font-family:"Oswald",sans-serif;font-weight:500;font-size:60px;letter-spacing:5px;line-height:70px}
.hero-title .sub{font-size:32px;font-weight:300;margin-top:6px}

/* about */
.about{height:208px}
.about h2{position:absolute;left:86px;top:62px}
.about .rule{position:absolute;left:86px;top:110px;margin:0}
.about p{position:absolute;left:264px;top:52px;width:850px;font-size:13px;line-height:24px}

/* offer */
.offer{height:515px;background:var(--pale-blue)}
.badge{position:absolute;left:104px;top:54px;width:142px;height:142px;border-radius:50%;border:4px solid var(--red)}
.offer-head{position:absolute;left:289px;top:58px;width:825px}
.offer-head h2{font-size:30px}
.offer-head .tag{font-size:15px;font-weight:500;color:var(--ink);margin-top:8px}
.offer-head p{margin-top:14px;font-size:13.5px}
.cards{position:absolute;left:86px;top:244px;width:1028px;display:flex;gap:40px}
.card{width:227px;height:204px;background:var(--white);border:1px solid var(--blue-soft);border-bottom:3px solid var(--red);text-align:center;padding:14px 10px 0}
.card svg{width:48px;height:48px;stroke:var(--blue-deep);fill:none;stroke-width:2}
.card h3{font-weight:500;font-size:19px;color:var(--ink);margin:10px 0 6px}
.card p{font-size:12px;line-height:19px}

/* process */
.process{height:567px;background:var(--pale-grey)}
.process h2{position:absolute;left:86px;top:56px;font-size:27px}
.process .rule{position:absolute;left:86px;top:102px;margin:0}
.process .intro{position:absolute;left:86px;top:124px;width:1028px;font-size:13px}
.diagram{position:absolute;left:86px;top:188px;width:570px;height:340px;background:linear-gradient(180deg,#e4e8ee,#dde2e9);border-radius:4px}
.risks{position:absolute;left:688px;top:218px;width:430px;list-style:none}
.risks li{display:flex;gap:22px;margin-bottom:28px}
.risk-icon{flex:none;width:50px;height:50px;border-radius:50%;background:var(--blue-deep);display:flex;align-items:center;justify-content:center}
.risk-icon svg{width:26px;height:26px;stroke:var(--white);fill:none;stroke-width:2}
.risks h4{font-weight:500;font-size:16px;color:var(--ink)}
.risks p{font-size:12.5px;line-height:21px;margin-top:4px}

/* visualisation */
.visual{height:505px;background:linear-gradient(120deg,#0a2a5a 0%,#0f3a78 50%,#0a2c60 100%)}
.device{position:absolute;left:46px;top:47px;width:561px;height:410px;border-radius:18px;background:linear-gradient(135deg,#2b2f36,#15181c)}
.device-screen{position:absolute;left:52px;top:30px;width:460px;height:350px;background:linear-gradient(160deg,#f2f3f4 0%,#d9dcdf 60%,#c8ccd0 100%)}
.visual-copy{position:absolute;left:649px;top:58px;width:470px;color:var(--white)}
.product{font-weight:600;font-size:21px;color:var(--white)}
.visual-copy h2{color:var(--white);font-size:32px;margin-top:6px}
.visual-copy .rule{margin-top:10px}
.visual-copy > p{font-size:13px;line-height:22px;margin-top:16px}
.features{display:grid;grid-template-columns:1fr 1fr;gap:20px 22px;margin-top:22px}
.features h4{font-weight:400;font-size:15.5px}
.features p{font-size:13px;line-height:21px}

/* partners */
.partners{height:283px}
.partners h2{position:absolute;left:86px;top:50px;font-size:29px}
.partners .rule{position:absolute;left:86px;top:96px;margin:0}
.partner-list{position:absolute;left:86px;top:146px;width:1028px;display:flex;justify-content:space-between;align-items:center;list-style:none}
.partner-list li{width:300px;text-align:center;font-size:40px;font-weight:500;color:var(--text)}

/* support */
.support{height:296px}
.support-bg{position:absolute;inset:0;background:linear-gradient(90deg,#1e1e1e 0%,#262626 55%,#4a4038 80%,#6a5a4c 100%)}
.support h2{position:absolute;left:86px;top:36px;color:var(--white);font-size:29px}
.support .rule{position:absolute;left:86px;top:82px;margin:0}
.support p{position:absolute;left:86px;top:114px;width:920px;color:var(--white);font-size:13px;line-height:24px}
.btn-ghost{position:absolute;left:86px;top:198px;width:140px;height:42px;border:1px solid var(--white);border-radius:21px;color:var(--white);font-size:15px;display:flex;align-items:center;justify-content:center}

/* contact */
.contact{height:441px}
.contact h2{position:absolute;left:86px;top:40px;font-size:29px}
.contact .rule{position:absolute;left:86px;top:86px;margin:0}
.field{position:absolute;border:1px solid var(--line);font-size:12px;color:var(--muted);padding:12px 12px}
.f-name{left:86px;top:128px;width:281px;height:44px}
.f-email{left:389px;top:128px;width:283px;height:44px}
.f-msg{left:86px;top:198px;width:586px;height:104px}
.btn-send{position:absolute;left:86px;top:330px;width:586px;height:38px;background:var(--red);color:var(--white);font-size:15px;display:flex;align-items:center;justify-content:center}
.details{position:absolute;left:725px;top:128px;width:400px}
.details h3{font-weight:500;font-size:20px;color:var(--ink);margin-bottom:26px}
.details li{list-style:none;display:flex;gap:18px;font-size:15px;color:var(--ink);line-height:24px;margin-bottom:30px}
.details svg{flex:none;width:18px;height:18px;fill:var(--ink);margin-top:3px}

/* footer */
.footer{height:62px;background:var(--ink)}
.footer p{position:absolute;left:86px;top:20px;font-size:12px;color:var(--white)}
</style>
</head>
<body>

<header class="hero">
  <div class="hero-bg" role="img" aria-label="Photo of a hand touching glowing hexagon network icons on a blue digital background"></div>
  <nav class="nav">
    <div class="brand"><span class="brand-mark"></span>QR248</div>
    <ul class="menu">
      <li class="active">Home</li><li>Who We are</li><li>Cyber Security</li><li>Visualisation</li><li>Trusted Partners</li><li>Support</li><li>Contact</li>
    </ul>
  </nav>
  <div class="hero-title">
    <h1>YOUR NETWORK</h1>
    <div class="sub">and Your Data is Your Business</div>
  </div>
</header>

<section class="about">
  <h2>About Us</h2><span class="rule"></span>
  <p>Sed ut perspiciatis unde omnis iste natus error sit voluptatem accusantium doloremque laudantium, totam rem aperiam, eaque ipsa quae ab illo inventore veritatis et quasi architecto beatae vitae dicta sunt explicabo. Nemo enim ipsam voluptatem quia voluptas sit aspernatur aut odit aut fugit, sed quia consequuntur magni dolores eos qui ratione voluptatem sequi nesciunt. Neque porro quisquam est, qui dolorem ipsum</p>
</section>

<section class="offer">
  <div class="badge"></div>
  <div class="offer-head">
    <h2>QR248 enables you to do that</h2>
    <div class="tag">Plan, Guard, Track, Steer – 365 days a year</div>
    <p>Defending that data, the network on which you move that data and understanding what that data is telling you is key to the success of every business.</p>
  </div>
  <div class="cards">
    <div class="card">
      <svg viewBox="0 0 48 48"><path d="M24 8a11 11 0 0 0-6 20v5h12v-5a11 11 0 0 0-6-20z"/><path d="M19 37h10M20 41h8M24 2v3M9 10l2 2M39 10l-2 2M5 22h3M40 22h3"/></svg>
      <h3>Plan</h3>
      <p>Baseline your OT communications with passive capture of your assets know your topology with confidence</p>
    </div>
    <div class="card">
      <svg viewBox="0 0 48 48"><path d="M24 4l16 6v12c0 11-7 19-16 22C15 41 8 33 8 22V10z"/><path d="M24 4v40M8 22h32"/></svg>
      <h3>Guard</h3>
      <p>Be alerted to any change in your baseline OT environment in real-time Pro-actively manage your threats</p>
    </div>
    <div class="card">
      <svg viewBox="0 0 48 48"><rect x="2" y="16" width="44" height="16"/><path d="M8 16v7M14 16v5M20 16v7M26 16v5M32 16v7M38 16v5"/></svg>
      <h3>Track</h3>
      <p>Baseline your OT communications with passive capture of your assets know your topology with confidence</p>
    </div>
    <div class="card">
      <svg viewBox="0 0 48 48"><path d="M6 12h36M6 24h36M6 36h36"/><circle cx="30" cy="12" r="4" fill="#fff"/><circle cx="16" cy="24" r="4" fill="#fff"/><circle cx="26" cy="36" r="4" fill="#fff"/></svg>
      <h3>Steer</h3>
      <p>Customise and present your dashboard in minutes Start managing your way, in minutes</p>
    </div>
  </div>
</section>

<section class="process">
  <h2>Process Control Cyber Security</h2><span class="rule"></span>
  <p class="intro">Sed ut perspiciatis unde omnis iste natus error sit voluptatem accusantium doloremque laudantium, totam rem aperiam, eaque ipsa quae ab illo inventore veritatis et quasi architecto beatae vitae dicta sunt explicabo. Nemo enim ipsam voluptatem quia voluptas</p>
  <div class="diagram" role="img" aria-label="Network diagram of an attacker, third party contractors, control networks and a firewalled plant IT network"></div>
  <ul class="risks">
    <li><span class="risk-icon"><svg viewBox="0 0 26 26"><rect x="4" y="4" width="18" height="18" rx="2"/><path d="M9 13l3 3 5-6"/></svg></span>
      <div><h4>Sed ut perspiciatis unde omnis iste</h4><p>Sed ut perspiciatis unde omnis iste natus error sit voluptatem accusantium doloremque</p></div></li>
    <li><span class="risk-icon"><svg viewBox="0 0 26 26"><path d="M13 3l8 3v7c0 5-4 9-8 10-4-1-8-5-8-10V6z"/><path d="M9 13l3 3 5-5"/></svg></span>
      <div><h4>Sed ut perspiciatis unde omnis iste</h4><p>Sed ut perspiciatis unde omnis iste natus error sit voluptatem accusantium doloremque</p></div></li>
    <li><span class="risk-icon"><svg viewBox="0 0 26 26"><path d="M2 13s4-7 11-7 11 7 11 7-4 7-11 7S2 13 2 13z"/><circle cx="13" cy="13" r="3"/></svg></span>
      <div><h4>Sed ut perspiciatis unde omnis iste</h4><p>Sed ut perspiciatis unde omnis iste natus error sit voluptatem accusantium doloremque</p></div></li>
  </ul>
</section>

<section class="visual">
  <div class="device" role="img" aria-label="Tablet and phone showing a KPI dashboard with coloured tiles and a site map">
    <div class="device-screen"></div>
  </div>
  <div class="visual-copy">
    <div class="product">ViewMetric</div>
    <h2>KPI Visualisation</h2><span class="rule"></span>
    <p>Sed ut perspiciatis unde omnis iste natus error sit voluptatem accusantium doloremque laudantium, totam rem aperiam, eaque ipsa quae ab illo inventore veritatis et quasi architecto beatae vitae dicta sunt explicabo. Nemo enim ipsam voluptatem quia voluptas</p>
    <div class="features">
      <div><h4>Read Data in Real-Time</h4><p>Leave your data where it makes sense and read</p></div>
      <div><h4>Simplify by Adding Context</h4><p>Transform raw data into intuitive KPIs everyone can understand</p></div>
      <div><h4>Read Data in Real-Time</h4><p>Leave your data where it makes sense and read</p></div>
      <div><h4>Simplify by Adding Context</h4><p>Transform raw data into intuitive KPIs everyone can understand .</p></div>
    </div>
  </div>
</section>

<section class="partners">
  <h2>Trusted Partners</h2><span class="rule"></span>
  <ul class="partner-list">
    <li>Belvanta</li><li>Korinex</li><li>Drumelo</li>
  </ul>
</section>

<section class="support">
  <div class="support-bg" role="img" aria-label="Photo of a support agent wearing a headset over a dark world map"></div>
  <h2>Support</h2><span class="rule"></span>
  <p>Sed ut perspiciatis unde omnis iste natus error sit voluptatem accusantium doloremque laudantium, totam rem aperiam, eaque ipsa quae ab illo inventore veritatis et quasi architecto beatae vitae dicta sunt explicabo.</p>
  <div class="btn-ghost">Get Support</div>
</section>

<section class="contact">
  <h2>Contact Us</h2><span class="rule"></span>
  <div class="field f-name">Name</div>
  <div class="field f-email">Email</div>
  <div class="field f-msg">Message</div>
  <div class="btn-send">Send Message</div>
  <div class="details">
    <h3>Contact Details</h3>
    <ul>
      <li><svg viewBox="0 0 18 18"><path d="M17 1L1 8l7 2 2 7z"/></svg><span>48 Harlow Row, Suite 12, Kestrel Bay, ON K7P 2R4<br>Canada</span></li>
      <li><svg viewBox="0 0 18 18"><path d="M4 1l3 4-2 2c1 3 3 5 6 6l2-2 4 3-2 3C8 17 1 10 1 3z"/></svg><span>2480 - 193 - 657</span></li>
      <li><svg viewBox="0 0 18 18"><path d="M1 6l8-5 8 5v10H1z"/><path d="M1 6l8 6 8-6" fill="none" stroke="#fff" stroke-width="1.5"/></svg><span>info@qr248.example</span></li>
    </ul>
  </div>
</section>

<footer class="footer">
  <p>Copyright © 2018. All rights reserved.</p>
</footer>

</body>
</html>
```